Vela Stewardship Business Card design

We need a creative business card design for our hospitality management company
We need the following information:
Our business Logo: Vela Stewardship
Name: Mara Dobrinsky
Phone number: 0458 317 642
Email: mara@velastewardship.com.au
Address: 214/53 Penrose Street, South Melbourne 3206
Web: www.velastewardship.com.au
I need the design to be a working file so that I can insert the names and numbers of the other staff members of our business.
The cards need to be 90 x 40mm
Thanks
Industry/Entity Type
Hospitality
Look and feel

```html
<!DOCTYPE html>
<html lang="en">
<head>
<meta charset="utf-8">
<title>Vela Stewardship Business Card</title>
<link rel="stylesheet" href="https://fonts.googleapis.com/css2?family=Open+Sans:wght@400&family=Play:wght@700&family=Roboto+Condensed:wght@700&display=swap">
<style>
  :root {
    --ink-night: #04070e;
    --ink-navy: #0d2159;
    --brand-blue: #2664dc;
    --paper-white: #ffffff;
    --silver: #d9dde3;
    --backdrop: #e9e6e1;
  }
  * { margin: 0; padding: 0; box-sizing: border-box; }
  html, body { width: 1200px; height: 900px; overflow: hidden; }
  body { background: var(--backdrop); position: relative; font-family: "Open Sans", Arial, sans-serif; }

  .card {
    position: absolute;
    width: 572px;
    height: 253px;
    overflow: hidden;
    box-shadow: 0 2px 6px rgba(0,0,0,0.25);
  }
  .card--front {
    left: 17px; top: 343px;
    background: linear-gradient(90deg, var(--ink-night) 0%, var(--ink-navy) 30%, var(--brand-blue) 75%, var(--brand-blue) 100%);
  }
  .card--back {
    left: 609px; top: 346px;
    background: linear-gradient(90deg, var(--brand-blue) 0%, var(--brand-blue) 15%, var(--ink-navy) 65%, var(--ink-night) 100%);
  }

  .holder-name {
    position: absolute;
    left: 0; right: 0; top: 62px;
    text-align: center;
    font-family: "Play", "Trebuchet MS", sans-serif;
    font-weight: 700;
    font-size: 30px;
    letter-spacing: 0.5px;
    color: var(--paper-white);
  }

  .contact-band {
    position: absolute;
    left: 0; right: 0; top: 168px; height: 59px;
    background: linear-gradient(90deg, var(--brand-blue) 0%, var(--brand-blue) 12%, var(--ink-navy) 60%, var(--ink-night) 100%);
    color: var(--paper-white);
    font-size: 12.5px;
  }
  .contact-row {
    position: absolute;
    left: 86px;
    display: flex;
    align-items: center;
    white-space: nowrap;
  }
  .contact-row--top { top: 10px; }
  .contact-row--bottom { top: 31px; }
  .contact-item { display: inline-flex; align-items: center; gap: 4px; }
  .contact-item + .contact-item { margin-left: 12px; }
  .contact-item--email { width: 210px; }
  .contact-icon { width: 15px; height: 15px; fill: var(--paper-white); flex: none; }

  .brand-lockup {
    position: absolute;
    left: 0; right: 0; top: 80px;
    display: flex;
    flex-direction: column;
    align-items: center;
    gap: 10px;
  }
  .brand-square {
    width: 62px; height: 62px;
    background: var(--silver);
  }
  .brand-name {
    font-family: "Roboto Condensed", Arial, sans-serif;
    font-weight: 700;
    font-size: 23px;
    color: var(--silver);
    letter-spacing: 0.3px;
  }
</style>
</head>
<body>

<section class="card card--front" aria-label="Business card front">
  <h1 class="holder-name">Mara Dobrinsky</h1>
  <div class="contact-band">
    <div class="contact-row contact-row--top">
      <span class="contact-item">
        <svg class="contact-icon" viewBox="0 0 16 16" aria-hidden="true"><rect x="1" y="3" width="14" height="11" rx="1"/><rect x="3" y="1" width="3" height="4" fill="#1a3f9a"/><rect x="8" y="6" width="5" height="6" fill="#1a3f9a"/></svg>
        0458 317 642
      </span>
      <span class="contact-item">
        <svg class="contact-icon" viewBox="0 0 16 16" aria-hidden="true"><path d="M1 6 L8 1 L15 6 V14 H1 Z"/><path d="M1 6 L8 11 L15 6" fill="none" stroke="#1a3a8a" stroke-width="1"/></svg>
        214/53 Penrose Street, South Melbourne 3206
      </span>
    </div>
    <div class="contact-row contact-row--bottom">
      <span class="contact-item contact-item--email">
        <svg class="contact-icon" viewBox="0 0 16 16" aria-hidden="true"><text x="0" y="13" font-size="15" font-family="Arial, sans-serif" fill="#fff">@</text></svg>
        mara@velastewardship.com.au
      </span>
      <span class="contact-item">
        <svg class="contact-icon" viewBox="0 0 16 16" aria-hidden="true"><g fill="none" stroke="#fff" stroke-width="1.2"><circle cx="8" cy="8" r="6.5"/><ellipse cx="8" cy="8" rx="3" ry="6.5"/><line x1="1.5" y1="8" x2="14.5" y2="8"/><line x1="2.5" y1="4.5" x2="13.5" y2="4.5"/><line x1="2.5" y1="11.5" x2="13.5" y2="11.5"/></g></svg>
        www.velastewardship.com.au
      </span>
    </div>
  </div>
</section>

<section class="card card--back" aria-label="Business card back">
  <div class="brand-lockup">
    <span class="brand-square" aria-hidden="true"></span>
    <span class="brand-name">VELA STEWARDSHIP</span>
  </div>
</section>

</body>
</html>
```